Breeze Horizon needs a "rack" brochure (4x9 inches) front and back

We need a rack brochure that will be distributed at hotels, airports...etc for an private airline company based at the Pelham-Corwick International Airport. We would like to see the use of the color of blues and the final product to communicate easy, reliable and affordable flights. (Breeze Horizon's guests are able to enjoy the glittering blue waters of the Abacos in just over an hour after boarding their flight.)

BReeze Horizon offers:
* Daily flights to Treasure Cay and Marsh Harbor
* First class service in every seat
* Pet-friendly flights
* On line booking
* VIP Passenger lounge
* Free Valet Parking
* Stress-free travel semi-private travel
* Private terminal no NPB security lines
* Convenient online booking @ FlyBreezeHorizon.com

Target Market(s)

25-60 couples and families traveling for pleasure on vacation or second homes.

Industry/Entity Type

Airline

Font styles to use
Sans Serif

Colors
33a6d7
4782bc
85cae6
cee9f5
0392cd

Requirements
Must have
• The additional two images I downloaded and sent (Via from www.filedriftbox.com)
• I am including the link. https://fd.xy/7k2pqwlnRZ. These two images were too large to upload
Nice to have
• Picture of the aircraft Stratus Wing 350
Should not have
• specific prices or flight schedule

```html
<!DOCTYPE html>
<html lang="en">
<head>
<meta charset="utf-8">
<title>Breeze Horizon Rack Brochure</title>
<link href="https://fonts.googleapis.com/css2?family=Lato:wght@400;700&family=Montserrat:wght@400&family=Oswald:wght@700&display=swap" rel="stylesheet">
<style>
  :root {
    --page-bg: #b9c9e6;
    --royal: #0a3ca8;
    --deep: #0d2f9e;
    --sky: #33a6d7;
    --aqua: #4dd3e6;
    --teal-text: #2bbcd0;
    --pale: #cee9f5;
    --ink: #3a3a3a;
    --grey: #555;
    --white: #fff;
  }
  * { margin: 0; padding: 0; box-sizing: border-box; }
  html, body { width: 1200px; height: 1200px; overflow: hidden; }
  body { background: var(--page-bg); position: relative; font-family: 'Lato', sans-serif; }

  .panel {
    position: absolute; top: 81px; width: 463px; height: 1040px; overflow: hidden;
    box-shadow: 0 4px 14px rgba(30, 50, 100, .25);
  }
  .panel--front { left: 114px; background: var(--royal); }
  .panel--back { left: 654px; background: var(--white); }
  .panel svg.shapes { position: absolute; inset: 0; }

  /* front */
  .front-title {
    position: absolute; top: 38px; width: 100%; text-align: center;
    font-family: 'Oswald', sans-serif; font-weight: 700; font-size: 68px; line-height: 1;
    color: var(--white); letter-spacing: 1px;
  }
  .front-promise {
    position: absolute; left: 46px; top: 120px; width: 367px; height: 54px;
    border: 1.5px solid var(--white);
    display: flex; align-items: center; justify-content: center; text-align: center;
    font-family: 'Montserrat', sans-serif; font-size: 15px; line-height: 21px; color: var(--white); letter-spacing: .5px;
  }
  .brand { position: absolute; top: 719px; left: 0; width: 100%; text-align: center; }
  .brand__dot {
    width: 112px; height: 112px; border-radius: 50%; background: var(--royal); margin: 0 auto 10px;
  }
  .brand__name {
    font-family: 'Lato', sans-serif; font-weight: 700; font-size: 22px; line-height: 26px;
    letter-spacing: 4px; color: var(--royal);
  }
  .front-web {
    position: absolute; left: 28px; top: 989px;
    font-family: 'Lato', sans-serif; font-weight: 700; font-size: 23px; line-height: 28px; color: var(--white);
  }
  .book-now {
    position: absolute; left: 315px; top: 897px; width: 128px; height: 128px; border-radius: 50%;
    background: var(--royal); border: 2px solid var(--white);
    display: flex; align-items: center; justify-content: center; text-align: center;
    font-family: 'Oswald', sans-serif; font-weight: 700; font-size: 34px; line-height: 1.15; color: var(--white);
  }

  /* back */
  .back-title {
    position: absolute; top: 35px; width: 100%; text-align: center;
    font-family: 'Oswald', sans-serif; font-weight: 700; font-size: 31px; line-height: 40px;
    color: var(--teal-text); letter-spacing: .5px;
  }
  .route {
    position: absolute; top: 87px; left: 36px; right: 36px; text-align: center;
    font-size: 16px; line-height: 20px; color: var(--grey); letter-spacing: .3px;
  }
  .offers-tag {
    position: absolute; top: 713px; left: 50%; transform: translateX(-50%);
    background: var(--aqua); color: var(--white); font-weight: 700; font-size: 16px; line-height: 19px;
    padding: 5px 12px; white-space: nowrap;
  }
  .offers { position: absolute; top: 765px; list-style: none; font-size: 14.5px; color: var(--ink); }
  .offers--left { left: 28px; }
  .offers--right { left: 266px; }
  .offers li { display: flex; align-items: center; gap: 6px; height: 25px; white-space: nowrap; }
  .offers svg { width: 17px; height: 17px; flex: none; }

  .contact-title {
    position: absolute; top: 944px; width: 100%; text-align: center; font-size: 15px; line-height: 18px;
    color: var(--aqua); letter-spacing: .3px;
  }
  .contact-line {
    position: absolute; left: 40px; display: flex; align-items: center; gap: 10px;
    color: var(--white); font-size: 15px; line-height: 20px;
  }
  .contact-line svg { width: 16px; height: 18px; flex: none; }
  .contact-line--address { top: 975px; }
  .contact-line--reach { top: 1003px; }
  .divider { width: 1px; height: 20px; background: rgba(255,255,255,.6); margin: 0 2px; }
</style>
</head>
<body>

<section class="panel panel--front">
  <svg class="shapes" width="463" height="1040" viewBox="0 0 463 1040">
    <defs>
      <linearGradient id="coastGrad" x1="0" y1="0" x2="0" y2="1">
        <stop offset="0" stop-color="#0a3ca8"/>
        <stop offset="0.35" stop-color="#1d6fd0"/>
        <stop offset="0.55" stop-color="#5aa8e0"/>
        <stop offset="0.72" stop-color="#5f8a58"/>
        <stop offset="0.85" stop-color="#e8e2d2"/>
        <stop offset="1" stop-color="#49c4e0"/>
      </linearGradient>
    </defs>
    <rect x="0" y="190" width="463" height="680" fill="url(#coastGrad)" role="img"
          aria-label="Photo of a twin-prop aircraft flying over a tropical beach with thatched umbrellas and palm trees"/>
    <path d="M0 825 C 150 800, 330 760, 463 715 L463 1040 L0 1040 Z" fill="var(--white)"/>
    <path d="M0 905 C 150 880, 330 880, 463 835 L463 860 C 330 905, 150 905, 0 925 Z" fill="var(--pale)"/>
    <path d="M0 920 C 160 905, 330 925, 463 880 L463 1040 L0 1040 Z" fill="var(--sky)"/>
    <path d="M0 936 C 170 925, 320 948, 463 902" fill="none" stroke="#85cae6" stroke-width="5"/>
  </svg>
  <h1 class="front-title">FLY WITH US</h1>
  <p class="front-promise">WE’LL DO EVERYTHING WE CAN TO MAKE<br>YOUR TRIP THE BEST EVER</p>
  <div class="brand">
    <div class="brand__dot"></div>
    <div class="brand__name">BREEZE HORIZON</div>
  </div>
  <p class="front-web">www.flybreezehorizon.com</p>
  <div class="book-now">BOOK<br>NOW</div>
</section>

<section class="panel panel--back">
  <svg class="shapes" width="463" height="1040" viewBox="0 0 463 1040">
    <defs>
      <linearGradient id="cabinGrad" x1="0" y1="0" x2="0" y2="1">
        <stop offset="0" stop-color="#8a7a66"/>
        <stop offset="0.5" stop-color="#d9c6a6"/>
        <stop offset="1" stop-color="#a89a86"/>
      </linearGradient>
      <linearGradient id="loungeGrad" x1="0" y1="0" x2="0" y2="1">
        <stop offset="0" stop-color="#1f9cc4"/>
        <stop offset="1" stop-color="#8a7560"/>
      </linearGradient>
      <linearGradient id="windowGrad" x1="0" y1="0" x2="1" y2="1">
        <stop offset="0" stop-color="#c9c4b8"/>
        <stop offset="1" stop-color="#6fb7b3"/>
      </linearGradient>
    </defs>
    <path d="M0 270 C 110 180, 300 130, 463 200 L463 230 C 300 170, 110 210, 0 290 Z" fill="var(--aqua)"/>
    <path d="M0 290 C 110 210, 300 175, 463 232 L463 560 C 380 610, 300 640, 226 640 C 140 640, 60 580, 0 530 Z" fill="var(--deep)"/>
    <path d="M0 300 C 110 225, 300 195, 463 250 L463 545 C 380 590, 300 620, 226 620 C 140 620, 60 565, 0 515 Z"
          fill="url(#cabinGrad)" role="img" aria-label="Photo of a private aircraft cabin with cream leather seats facing the cockpit"/>
    <path d="M0 560 C 70 610, 150 650, 226 655 C 310 660, 390 620, 463 570 L463 590 C 390 640, 310 680, 226 675 C 150 670, 70 630, 0 580 Z" fill="var(--aqua)"/>
    <circle cx="122" cy="587" r="88" fill="var(--deep)"/>
    <circle cx="122" cy="587" r="83" fill="var(--aqua)"/>
    <circle cx="122" cy="587" r="78" fill="url(#loungeGrad)" role="img" aria-label="Photo of the passenger lounge with armchairs"/>
    <circle cx="326" cy="599" r="88" fill="var(--deep)"/>
    <circle cx="326" cy="599" r="83" fill="var(--aqua)"/>
    <circle cx="326" cy="599" r="78" fill="url(#windowGrad)" role="img" aria-label="Photo of a passenger looking out an aircraft window"/>
    <path d="M0 950 C 120 890, 290 880, 463 990 L463 1000 C 290 895, 120 905, 0 965 Z" fill="var(--aqua)"/>
    <path d="M0 965 C 120 910, 290 905, 463 1000 L463 1040 L0 1040 Z" fill="var(--deep)"/>
  </svg>

  <h2 class="back-title">SCHEDULED DAILY SERVICE</h2>
  <p class="route">FROM MARSH HARBOUR/TREASURE CAY TO<br>PELHAM-CORWICK INTERNATIONAL AIRPORT</p>

  <div class="offers-tag">BREEZE HORIZON OFFERS:</div>
  <ul class="offers offers--left">
    <li><svg viewBox="0 0 18 18"><circle cx="8" cy="10" r="6.5" fill="none" stroke="#4a6a8a" stroke-width="1.5"/><path d="M5 9.5 L8 12.5 L16 3" fill="none" stroke="#2bbcd0" stroke-width="2"/></svg>First class services in every seat</li>
    <li><svg viewBox="0 0 18 18"><circle cx="8" cy="10" r="6.5" fill="none" stroke="#4a6a8a" stroke-width="1.5"/><path d="M5 9.5 L8 12.5 L16 3" fill="none" stroke="#2bbcd0" stroke-width="2"/></svg>Pet-friendly flights</li>
    <li><svg viewBox="0 0 18 18"><circle cx="8" cy="10" r="6.5" fill="none" stroke="#4a6a8a" stroke-width="1.5"/><path d="M5 9.5 L8 12.5 L16 3" fill="none" stroke="#2bbcd0" stroke-width="2"/></svg>Convenient online booking</li>
    <li><svg viewBox="0 0 18 18"><circle cx="8" cy="10" r="6.5" fill="none" stroke="#4a6a8a" stroke-width="1.5"/><path d="M5 9.5 L8 12.5 L16 3" fill="none" stroke="#2bbcd0" stroke-width="2"/></svg>Vip passenger lounge</li>
  </ul>
  <ul class="offers offers--right">
    <li><svg viewBox="0 0 18 18"><circle cx="8" cy="10" r="6.5" fill="none" stroke="#4a6a8a" stroke-width="1.5"/><path d="M5 9.5 L8 12.5 L16 3" fill="none" stroke="#2bbcd0" stroke-width="2"/></svg>Free valet parking</li>
    <li><svg viewBox="0 0 18 18"><circle cx="8" cy="10" r="6.5" fill="none" stroke="#4a6a8a" stroke-width="1.5"/><path d="M5 9.5 L8 12.5 L16 3" fill="none" stroke="#2bbcd0" stroke-width="2"/></svg>Stress-free travel</li>
    <li><svg viewBox="0 0 18 18"><circle cx="8" cy="10" r="6.5" fill="none" stroke="#4a6a8a" stroke-width="1.5"/><path d="M5 9.5 L8 12.5 L16 3" fill="none" stroke="#2bbcd0" stroke-width="2"/></svg>Private terminal</li>
  </ul>

  <p class="contact-title">CONTACT INFO</p>
  <p class="contact-line contact-line--address">
    <svg viewBox="0 0 16 18"><path d="M8 1 C4 1 2 4 2 6.5 C2 10 8 17 8 17 C8 17 14 10 14 6.5 C14 4 12 1 8 1 Z" fill="#fff"/><circle cx="8" cy="6.5" r="2.3" fill="#0d2f9e"/></svg>
    2750 Skyview Lane Pelham.FL32990
  </p>
  <p class="contact-line contact-line--reach">
    <svg viewBox="0 0 16 18"><path d="M4 2 L6.5 2 L7.5 6 L5.8 7.4 C6.6 9.6 7.8 11.2 9.6 12.3 L11 10.7 L14 12 L14 15 C14 16 13 16.5 12 16.3 C7 15.5 3 11 2.5 5 C2.4 3 3 2 4 2 Z" fill="#fff"/></svg>
    +1 555-014-2290
    <span class="divider"></span>
    <svg viewBox="0 0 18 14"><rect x="1" y="2" width="16" height="10" fill="#fff"/><path d="M1 2 L9 8 L17 2" fill="none" stroke="#0d2f9e" stroke-width="1.3"/></svg>
    www.flybreezehorizon.com
  </p>
</section>

</body>
</html>
```